Mobile Printer company needs a corporate PowerPoint Template

Looking to get a corporate PowerPoint template created to sue for a variety of presentations to customer, resellers, and partners. Would like the color scheme to include Blue, black, and grey to match our corporate colors. Since we are a mobile technology company, I'd like the template to have modern tech look to it. Attached is our current PowerPoint that we use for new partners.

Target Market(s)

public safety, hospitality, route accounting, DSD, warehousing/logistics, health care, etc.

Industry/Entity Type

Too many to list

Colors
0054AA
0677BA
7BADD7
CADEEF
E8F1F8

Requirements
Must have
• Quorvane logo, places to drop in photos
Nice to have
• attractive graphics to display excel data

```html
<!DOCTYPE html>
<html lang="en">
<head>
<meta charset="utf-8">
<title>Quorvane Corporate Presentation Template</title>
<link href="https://fonts.googleapis.com/css2?family=Montserrat:wght@400;500;600;700;800;900&display=swap" rel="stylesheet">
<style>
:root{
  --blue-deep:#0054AA;
  --blue:#0677BA;
  --blue-bright:#1b8fd3;
  --blue-soft:#7BADD7;
  --blue-pale:#CADEEF;
  --blue-mist:#E8F1F8;
  --ink:#1d1d1f;
  --charcoal:#2b2c2f;
  --grey:#8a8d92;
  --grey-light:#e2e2e4;
  --stage:#d9d8db;
  --white:#ffffff;
}
*{margin:0;padding:0;box-sizing:border-box}
html,body{width:1200px;height:2449px;overflow:hidden}
body{font-family:'Montserrat',Arial,sans-serif;color:var(--ink);
  background:linear-gradient(180deg,#c9ccd2 0,#e6e7ea 420px,#dedcdc 740px,var(--stage) 741px,var(--stage) 100%);
  position:relative}

/* brand wordmark */
.wordmark{font-family:'Montserrat',Arial,sans-serif;font-weight:800;color:var(--ink);letter-spacing:.5px;line-height:1;position:absolute;white-space:nowrap}

/* hero */
.hero-mark{top:44px;left:930px;font-size:38px}
.hero-slide{position:absolute;left:263px;top:170px;transform:scale(1.2);transform-origin:0 0;box-shadow:0 20px 40px rgba(0,0,0,.18)}

/* slide frame */
.slide{position:absolute;width:562px;height:316px;background:var(--white);overflow:hidden}
.c1{left:28px}.c2{left:610px}
.r1{top:761px}.r2{top:1096px}.r3{top:1431px}.r4{top:1766px}.r5{top:2101px}
.layer{position:absolute;left:0;top:0;width:562px;height:316px}

/* title slides */
.title-block{position:absolute;left:50px;color:var(--white)}
.title{font-weight:900;font-size:28px;line-height:31px;letter-spacing:.6px}
.subtitle{font-size:12px;font-weight:500;margin-top:8px}
.date{font-size:6.5px;letter-spacing:.8px;margin-top:15px}
.url-btn{display:inline-block;margin-top:14px;width:92px;height:16px;border:1px solid var(--white);border-radius:2px;font-size:6px;text-align:center;line-height:14px;letter-spacing:.5px}
.title-mark{font-size:23px;left:52px;top:253px}
.copy{position:absolute;font-size:5px;color:var(--grey);letter-spacing:.6px;width:100%;text-align:center}
.product{position:absolute;left:372px;top:180px;width:130px;height:110px;border-radius:14px;background:linear-gradient(135deg,#5a5d62,#24262a)}
.tagline{position:absolute;top:22px;font-size:6.5px;color:var(--blue);letter-spacing:.5px;font-weight:500}
.top-mark{font-size:22px;top:29px}

/* content footer */
.foot-mark{font-size:13px;left:12px;top:284px}
.foot-bar{position:absolute;left:108px;top:287px;width:440px;height:11px;border-radius:6px;background:var(--blue)}
.foot-bar span{position:absolute;right:22px;top:2px;font-size:4.6px;color:var(--white)}
.foot-bar i{position:absolute;right:1px;top:1px;width:9px;height:9px;border-radius:50%;background:var(--blue-soft);font-style:normal;font-size:4.5px;color:var(--white);text-align:center;line-height:9px}

.body-text{font-size:5.6px;line-height:6.6px;color:#4a4c50}
.body-text p+p{margin-top:5px}

/* about */
.about-panel{position:absolute;left:0;top:0;width:218px;height:316px;background:linear-gradient(160deg,#3a3b3f,#1f2023)}
.about-photo{position:absolute;left:33px;top:33px;width:212px;height:219px;border:2px solid var(--white);background:linear-gradient(180deg,#8fa7c0 0,#e9a55a 55%,#3b2a1c 100%)}
.about-head{position:absolute;left:271px;top:57px;font-size:17px;font-weight:700;letter-spacing:.5px}
.about-text{position:absolute;left:271px;top:88px;width:252px}

/* numbered steps */
.h-left{position:absolute;left:45px;top:44px;font-size:17px;font-weight:700}
.lead{position:absolute;left:45px;top:91px;width:205px;font-size:7px;line-height:8px;color:var(--blue)}
.step-text{position:absolute;left:45px;top:138px;width:200px}
.step{position:absolute;left:286px;width:234px;height:59px;border-radius:6px;color:var(--white);box-shadow:0 2px 3px rgba(0,0,0,.25)}
.step b{position:absolute;left:17px;top:12px;font-size:29px;font-weight:800}
.step em{position:absolute;left:52px;top:12px;width:1px;height:36px;background:rgba(255,255,255,.6)}
.step span{position:absolute;left:60px;top:12px;width:165px;font-size:5.4px;line-height:6px}
.s1{top:44px;background:var(--blue)}.s2{top:113px;background:var(--blue-soft)}.s3{top:182px;background:var(--ink)}

/* divisions */
.div-band{position:absolute;left:0;top:0;width:562px;height:120px;background:linear-gradient(160deg,#3a3b3f,#1f2023)}
.div-title{position:absolute;top:24px;width:100%;text-align:center;font-size:17px;font-weight:700;color:var(--blue-bright)}
.div-card{position:absolute;top:72px;width:233px;height:97px;background:var(--white);border:1px solid var(--grey-light)}
.div-card .shot{position:absolute;left:70px;top:20px;width:93px;height:55px;border-radius:4px;background:linear-gradient(135deg,#6d7076,#26282c)}
.div-name{position:absolute;top:181px;font-size:10px;font-weight:700;color:var(--blue)}
.div-text{position:absolute;top:198px;width:222px}
.div-est{position:absolute;top:236px;font-size:5.5px;font-weight:700;color:var(--blue)}

/* team */
.center-head{position:absolute;top:25px;width:100%;text-align:center;font-size:17px;font-weight:700}
.member{position:absolute;top:76px;width:110px;text-align:center}
.member .portrait{width:70px;height:102px;margin:0 auto;background:linear-gradient(180deg,#d8d9db,#8d8f93 60%,#2c2f36)}
.member h4{font-size:9.5px;font-weight:700;color:var(--blue);margin-top:9px}
.member h5{font-size:6px;font-weight:400;color:var(--blue-soft);margin-top:3px}
.member p{font-size:5.4px;line-height:6px;color:#4a4c50;margin-top:5px}

/* charts */
.stat{position:absolute;top:76px;width:140px;text-align:center}
.stat svg{display:block;margin:0 auto}
.stat h4{font-size:9.5px;font-weight:700;margin-top:14px}
.stat p{font-size:5.4px;line-height:6px;color:#4a4c50;margin-top:5px;padding:0 16px}

/* thank you */
.thanks{position:absolute;left:50px;top:112px;font-size:26px;font-weight:800;color:var(--white)}
.thanks-rule{position:absolute;left:50px;top:150px;width:160px;height:1px;background:var(--blue-pale)}
.contact{position:absolute;left:50px;top:161px;color:var(--white)}
.contact h4{font-size:11px;font-weight:700}
.contact .addr{font-size:7px;margin-top:7px}
.contact ul{list-style:none;margin-top:9px}
.contact li{font-size:7px;display:flex;align-items:center;gap:8px;margin-top:5px}
</style>
</head>
<body>

<div class="wordmark hero-mark">QUORVANE</div>

<!-- hero title slide -->
<section class="slide hero-slide">
  <svg class="layer" viewBox="0 0 562 316" role="img" aria-label="Team silhouettes in an office, blue tinted">
    <defs><linearGradient id="gA0" x1="0" y1="0" x2="1" y2="1"><stop offset="0" stop-color="#0a7dc4"/><stop offset="1" stop-color="#2096d8"/></linearGradient></defs>
    <path d="M0 0H562V246C500 238 450 212 360 214C260 216 150 222 0 232Z" fill="url(#gA0)"/>
  </svg>
  <div class="title-block" style="top:44px">
    <div class="title">PRESENTATION<br>TITLE GOES HERE</div>
    <div class="subtitle">Subtitle of Presentation Goes Here</div>
    <div class="date">Monday, February 13, 2023</div>
    <div class="url-btn">www.quorvane.com</div>
  </div>
  <div class="product" role="img" aria-label="Mobile printer product photo"></div>
  <div class="wordmark title-mark">QUORVANE</div>
  <div class="copy" style="top:301px">© Copyright 2023 Quorvane®, L.L.C.</div>
</section>

<!-- row 1 -->
<section class="slide c1 r1">
  <svg class="layer" viewBox="0 0 562 316" role="img" aria-label="Team silhouettes in an office, blue tinted">
    <defs><linearGradient id="gA1" x1="0" y1="0" x2="1" y2="1"><stop offset="0" stop-color="#0a7dc4"/><stop offset="1" stop-color="#2096d8"/></linearGradient></defs>
    <path d="M0 0H562V246C500 238 450 212 360 214C260 216 150 222 0 232Z" fill="url(#gA1)"/>
  </svg>
  <div class="title-block" style="top:44px">
    <div class="title">PRESENTATION<br>TITLE GOES HERE</div>
    <div class="subtitle">Subtitle of Presentation Goes Here</div>
    <div class="date">Monday, February 13, 2023</div>
    <div class="url-btn">www.quorvane.com</div>
  </div>
  <div class="product" role="img" aria-label="Mobile printer product photo"></div>
  <div class="wordmark title-mark">QUORVANE</div>
  <div class="copy" style="top:301px">© Copyright 2023 Quorvane®, L.L.C.</div>
</section>

<section class="slide c2 r1">
  <svg class="layer" viewBox="0 0 562 316" role="img" aria-label="Glass skyscrapers from below, blue tinted">
    <defs><linearGradient id="gA2" x1="0" y1="0" x2="1" y2="1"><stop offset="0" stop-color="#0a7dc4"/><stop offset=".6" stop-color="#1c8fd3"/><stop offset="1" stop-color="#4aa6de"/></linearGradient></defs>
    <path d="M0 0H562V246C500 238 450 212 360 214C260 216 150 222 0 232Z" fill="url(#gA2)"/>
  </svg>
  <div class="title-block" style="top:44px">
    <div class="title">PRESENTATION<br>TITLE GOES HERE</div>
    <div class="subtitle">Subtitle of Presentation Goes Here</div>
    <div class="date">Monday, February 13, 2023</div>
    <div class="url-btn">www.quorvane.com</div>
  </div>
  <div class="product" role="img" aria-label="Mobile printer product photo"></div>
  <div class="wordmark title-mark">QUORVANE</div>
  <div class="copy" style="top:301px">© Copyright 2023 Quorvane®, L.L.C.</div>
</section>

<!-- row 2 -->
<section class="slide c1 r2">
  <svg class="layer" viewBox="0 0 562 316" role="img" aria-label="Glass skyscrapers from below, blue tinted">
    <defs><linearGradient id="gC1" x1="0" y1="0" x2="1" y2="1"><stop offset="0" stop-color="#0a7dc4"/><stop offset="1" stop-color="#3aa0dc"/></linearGradient></defs>
    <path d="M0 84C120 78 220 58 330 54C430 52 500 64 562 84V295H0Z" fill="url(#gC1)"/>
  </svg>
  <div class="wordmark top-mark" style="left:30px">QUORVANE</div>
  <div class="tagline" style="right:34px">Ready. Rugged. Reliable.</div>
  <div class="title-block" style="top:119px">
    <div class="title">PRESENTATION<br>TITLE GOES HERE</div>
    <div class="subtitle">Subtitle of Presentation Goes Here</div>
    <div class="date">Monday, February 13, 2023</div>
    <div class="url-btn">www.quorvane.com</div>
  </div>
  <div class="copy" style="top:302px">© Copyright 2023 Quorvane®, L.L.C.</div>
</section>

<section class="slide c2 r2">
  <svg class="layer" viewBox="0 0 562 316" role="img" aria-label="Glass skyscrapers from below, blue tinted">
    <defs><linearGradient id="gC2" x1="0" y1="0" x2="1" y2="1"><stop offset="0" stop-color="#0a7dc4"/><stop offset="1" stop-color="#3aa0dc"/></linearGradient></defs>
    <path d="M0 84C62 64 132 52 232 54C342 58 442 78 562 84V295H0Z" fill="url(#gC2)"/>
  </svg>
  <div class="tagline" style="left:50px">Ready. Rugged. Reliable.</div>
  <div class="wordmark top-mark" style="right:36px">QUORVANE</div>
  <div class="title-block" style="top:107px">
    <div class="title">PRESENTATION<br>TITLE GOES HERE</div>
    <div class="subtitle">Subtitle of Presentation Goes Here</div>
    <div class="date">Monday, February 13, 2023</div>
    <div class="url-btn">www.quorvane.com</div>
  </div>
  <div class="copy" style="top:302px">© Copyright 2023 Quorvane®, L.L.C.</div>
</section>

<!-- row 3 -->
<section class="slide c1 r3">
  <div class="about-panel"></div>
  <div class="about-photo" role="img" aria-label="Business team silhouetted against a sunset city window"></div>
  <h2 class="about-head">ABOUT US</h2>
  <div class="about-text body-text">
    <p>As a global leader in business printers, both rugged mobile and high-speed multi-part form dot matrix, our name has long been linked with dependable printing for over 35 years. We supply printing solutions to many Fortune 500 firms, SMBs and public agencies worldwide.</p>
    <p>Our mobile printers are rugged direct thermal units built for field service, route accounting, manufacturing, retail, transport, public safety, hospitality, warehousing and delivery. Our dot matrix line handles the toughest multi-part forms with single and dual-track printers, all backed by strong support and complete warranties.</p>
    <p>We partner with software and hardware makers, system integrators and resellers to deliver cost-effective mobile business solutions for a wide range of uses.</p>
  </div>
  <div class="wordmark foot-mark" style="color:var(--white)">QUORVANE</div>
  <div class="foot-bar"><span>© Copyright 2023 Quorvane®, L.L.C.</span><i>3</i></div>
</section>

<section class="slide c2 r3">
  <h2 class="h-left">Heading Goes Here</h2>
  <p class="lead">Fermentum, Nisi Mauris Convallis Nunc, Ut Luctus Nunc Nisl Id Ex. Nam Semper Tristique Mauris, Et Vestibulum Leo Fringilla Vel.</p>
  <div class="step-text body-text">
    <p>Nunc vitae semper dui. Integer venenatis, tellus sit amet interdum pretium, erat neque rhoncus turpis, a aliquam augue ligula eget erat. Nunc placerat, arcu nec mattis fermentum, nisi mauris convallis nunc, ut luctus nunc nisl id ex. Nam semper tristique mauris, et vestibulum leo fringilla vel.</p>
    <p>Nunc vitae semper dui. Integer venenatis, tellus sit amet interdum pretium, erat neque rhoncus turpis, a aliquam augue ligula eget erat. Nunc placerat, arcu nec mattis fermentum, nisi mauris convallis nunc, ut luctus nunc nisl id ex. Nam semper tristique mauris, et vestibulum leo fringilla vel.</p>
  </div>
  <div class="step s1"><b>1</b><em></em><span>Phasellus eget commodo arcu. Nunc vitae semper dui. Integer venenatis, tellus sit amet interdum pretium, erat neque rhoncus turpis, a aliquam augue ligula eget erat. Nunc placerat, arcu nec mattis fermentum.</span></div>
  <div class="step s2"><b>2</b><em></em><span>Phasellus eget commodo arcu. Nunc vitae semper dui. Integer venenatis, tellus sit amet interdum pretium, erat neque rhoncus turpis, a aliquam augue ligula eget erat. Nunc placerat, arcu nec mattis fermentum.</span></div>
  <div class="step s3"><b>3</b><em></em><span>Phasellus eget commodo arcu. Nunc vitae semper dui. Integer venenatis, tellus sit amet interdum pretium, erat neque rhoncus turpis, a aliquam augue ligula eget erat. Nunc placerat, arcu nec mattis fermentum.</span></div>
  <div class="wordmark foot-mark">QUORVANE</div>
  <div class="foot-bar"><span>© Copyright 2023 Quorvane®, L.L.C.</span><i>4</i></div>
</section>

<!-- row 4 -->
<section class="slide c1 r4">
  <div class="div-band"></div>
  <h2 class="div-title">Quorvane Divisions</h2>
  <div class="div-card" style="left:31px"><div class="shot" role="img" aria-label="Impact dot matrix printers"></div></div>
  <div class="div-card" style="left:297px"><div class="shot" role="img" aria-label="Mobile thermal printer range"></div></div>
  <h3 class="div-name" style="left:36px">Impact Printers</h3>
  <p class="div-text body-text" style="left:36px">A leading global provider of innovative, heavy-duty dot matrix printers. Top companies count on the rugged reliability, superior technology and advanced forms handling of our dot matrix printers.</p>
  <div class="div-est" style="left:36px">• Established 1980</div>
  <h3 class="div-name" style="left:301px">Mobile Printers</h3>
  <p class="div-text body-text" style="left:301px">Mobile printers for mobile people. Our mobile thermal printers are designed to withstand industrial use in the field and offer reliable on-demand printing wherever your business takes place.</p>
  <div class="div-est" style="left:301px">• Established 2005</div>
  <div class="wordmark foot-mark">QUORVANE</div>
  <div class="foot-bar"><span>© Copyright 2023 Quorvane®, L.L.C.</span><i>5</i></div>
</section>

<section class="slide c2 r4">
  <h2 class="center-head">Meet Our Team</h2>
  <div class="member" style="left:44px"><div class="portrait" role="img" aria-label="Team member portrait photo"></div><h4>Person Name</h4><h5>Job Title Goes Here</h5><p>Lorem ipsum dolor sit amet, consectetur adipiscing elit. Vivamus eu dui ex. Curabitur dapibus dignissim dui, in molestie metus.</p></div>
  <div class="member" style="left:165px"><div class="portrait" role="img" aria-label="Team member portrait photo"></div><h4>Person Name</h4><h5>Job Title Goes Here</h5><p>Lorem ipsum dolor sit amet, consectetur adipiscing elit. Vivamus eu dui ex. Curabitur dapibus dignissim dui, in molestie metus.</p></div>
  <div class="member" style="left:287px"><div class="portrait" role="img" aria-label="Team member portrait photo"></div><h4>Person Name</h4><h5>Job Title Goes Here</h5><p>Lorem ipsum dolor sit amet, consectetur adipiscing elit. Vivamus eu dui ex. Curabitur dapibus dignissim dui, in molestie metus.</p></div>
  <div class="member" style="left:408px"><div class="portrait" role="img" aria-label="Team member portrait photo"></div><h4>Person Name</h4><h5>Job Title Goes Here</h5><p>Lorem ipsum dolor sit amet, consectetur adipiscing elit. Vivamus eu dui ex. Curabitur dapibus dignissim dui, in molestie metus.</p></div>
  <div class="wordmark foot-mark">QUORVANE</div>
  <div class="foot-bar"><span>© Copyright 2023 Quorvane®, L.L.C.</span><i>6</i></div>
</section>

<!-- row 5 -->
<section class="slide c1 r5">
  <h2 class="center-head">Heading Goes Here</h2>
  <div class="stat" style="left:56px">
    <svg width="120" height="120" viewBox="0 0 120 120">
      <circle cx="60" cy="60" r="52" fill="none" stroke="var(--grey-light)" stroke-width="10"/>
      <circle cx="60" cy="60" r="52" fill="none" stroke="var(--blue)" stroke-width="10" stroke-dasharray="114.4 326.7" transform="rotate(-90 60 60)"/>
      <text x="60" y="67" text-anchor="middle" font-family="Montserrat,Arial,sans-serif" font-weight="700" font-size="20" fill="var(--blue)">35<tspan font-size="10">%</tspan></text>
    </svg>
    <h4 style="color:var(--blue)">Heading Goes Here</h4>
    <p>Lorem ipsum dolor sit amet, consectetur adipiscing elit. Vivamus eu dui ex. Curabitur dapibus dignissim dui, in molestie metus.</p>
  </div>
  <div class="stat" style="left:211px">
    <svg width="120" height="120" viewBox="0 0 120 120">
      <circle cx="60" cy="60" r="52" fill="none" stroke="var(--grey-light)" stroke-width="10"/>
      <circle cx="60" cy="60" r="52" fill="none" stroke="var(--blue-soft)" stroke-width="10" stroke-dasharray="212.4 326.7" transform="rotate(-90 60 60)"/>
      <text x="60" y="67" text-anchor="middle" font-family="Montserrat,Arial,sans-serif" font-weight="700" font-size="20" fill="var(--blue-soft)">65<tspan font-size="10">%</tspan></text>
    </svg>
    <h4 style="color:var(--blue-soft)">Heading Goes Here</h4>
    <p>Lorem ipsum dolor sit amet, consectetur adipiscing elit. Vivamus eu dui ex. Curabitur dapibus dignissim dui, in molestie metus.</p>
  </div>
  <div class="stat" style="left:366px">
    <svg width="120" height="120" viewBox="0 0 120 120">
      <circle cx="60" cy="60" r="52" fill="none" stroke="var(--grey-light)" stroke-width="10"/>
      <circle cx="60" cy="60" r="52" fill="none" stroke="var(--ink)" stroke-width="10" stroke-dasharray="277.7 326.7" transform="rotate(-90 60 60)"/>
      <text x="60" y="67" text-anchor="middle" font-family="Montserrat,Arial,sans-serif" font-weight="700" font-size="20" fill="var(--ink)">85<tspan font-size="10">%</tspan></text>
    </svg>
    <h4>Heading Goes Here</h4>
    <p>Lorem ipsum dolor sit amet, consectetur adipiscing elit. Vivamus eu dui ex. Curabitur dapibus dignissim dui, in molestie metus.</p>
  </div>
  <div class="wordmark foot-mark">QUORVANE</div>
  <div class="foot-bar"><span>© Copyright 2023 Quorvane®, L.L.C.</span><i>7</i></div>
</section>

<section class="slide c2 r5">
  <svg class="layer" viewBox="0 0 562 316" role="img" aria-label="Glass skyscrapers from below, blue tinted">
    <defs><linearGradient id="gT" x1="0" y1="0" x2="1" y2="1"><stop offset="0" stop-color="#0a7dc4"/><stop offset="1" stop-color="#3aa0dc"/></linearGradient></defs>
    <path d="M0 70C62 52 132 44 232 46C342 50 442 66 562 64V296H0Z" fill="url(#gT)"/>
  </svg>
  <div class="wordmark top-mark" style="right:36px;top:24px">QUORVANE</div>
  <h2 class="thanks">Thank You!</h2>
  <div class="thanks-rule"></div>
  <div class="contact">
    <h4>Contact Us</h4>
    <div class="addr">1820 Harbor Point Road, Fairhaven, MI 49010</div>
    <ul>
      <li><svg width="9" height="9" viewBox="0 0 24 24"><path d="M6.6 10.8a15 15 0 0 0 6.6 6.6l2.2-2.2a1 1 0 0 1 1-.25 11.4 11.4 0 0 0 3.6.57 1 1 0 0 1 1 1V20a1 1 0 0 1-1 1A17 17 0 0 1 3 4a1 1 0 0 1 1-1h3.5a1 1 0 0 1 1 1c0 1.25.2 2.45.57 3.57a1 1 0 0 1-.25 1z" fill="#fff"/></svg>555.014.3200</li>
      <li><svg width="9" height="9" viewBox="0 0 24 24"><circle cx="12" cy="12" r="4" fill="none" stroke="#fff" stroke-width="2.4"/><path d="M16 8v5a3 3 0 0 0 6 0v-1a10 10 0 1 0-4 8" fill="none" stroke="#fff" stroke-width="2.4"/></svg>info@quorvane.com</li>
      <li><svg width="9" height="9" viewBox="0 0 24 24"><circle cx="12" cy="12" r="10" fill="none" stroke="#fff" stroke-width="2"/><ellipse cx="12" cy="12" rx="4.5" ry="10" fill="none" stroke="#fff" stroke-width="2"/><path d="M2 12h20" stroke="#fff" stroke-width="2"/></svg>https://www.quorvane.com</li>
    </ul>
  </div>
  <div class="copy" style="top:303px">© Copyright 2023 Quorvane®, L.L.C.</div>
</section>

</body>
</html>
```